Brin’s Beauty. Coffee Scrub Skincare

Graphic design for my Coffee Scrub skin care business. Brin’s Beauty. To go on the packaging. Fun with pastel colours, but still clean and professional. See attached photos on similar businesses packaging. I like the “Tala & Wren” font (see attached photo).

Things to write on the packaging: Brin’s Beauty. Recycled Coffee scrub. Coconut and Chocolate. Recycled packaging. Vegan. Not tested on animal. Recycled coffee. Pink Australian clay. 150g 5.29 oz. Made in Australia.

```html
<!DOCTYPE html>
<html lang="en">
<head>
<meta charset="utf-8">
<title>Brin’s Beauty – Recycled Coffee Scrub Packaging</title>
<link href="https://fonts.googleapis.com/css2?family=Quicksand:wght@500;600&family=Sofia+Sans+Extra+Condensed:wght@300;400&display=swap" rel="stylesheet">
<style>
  :root {
    --backdrop: #9e9a95;
    --plum: #6b3445;
    --plum-soft: #7d4a58;
    --label: #ffffff;
    --pink: #f2c3c1;
    --blush: #f6dcd6;
    --tan: #e4c2b3;
    --sage: #bfe0b3;
    --leaf: #5fae82;
    --cocoa: #a86d6c;
  }
  * { box-sizing: border-box; margin: 0; padding: 0; }
  html, body { width: 1200px; height: 900px; overflow: hidden; }
  body {
    background: var(--backdrop);
    font-family: "Quicksand", sans-serif;
    color: var(--plum);
    position: relative;
  }
  .pouch {
    position: absolute;
    top: 180px;
    width: 360px;
    height: 540px;
    box-shadow: 0 10px 24px rgba(0,0,0,0.18);
    overflow: hidden;
  }
  .pouch--front { left: 210px; }
  .pouch--back { left: 630px; }

  .pouch__artwork {
    position: absolute; inset: 0;
    background:
      radial-gradient(circle at 80% 12%, var(--tan) 0 22%, transparent 23%),
      radial-gradient(ellipse at 12% 15%, var(--leaf) 0 12%, transparent 13%),
      radial-gradient(ellipse at 90% 55%, var(--sage) 0 20%, transparent 21%),
      radial-gradient(ellipse at 15% 90%, var(--cocoa) 0 14%, transparent 15%),
      linear-gradient(160deg, var(--blush) 0%, var(--sage) 35%, var(--blush) 60%, var(--pink) 85%, var(--sage) 100%);
  }
  .pouch--back .pouch__artwork {
    background:
      radial-gradient(circle at 25% 12%, var(--tan) 0 22%, transparent 23%),
      radial-gradient(ellipse at 88% 18%, var(--leaf) 0 12%, transparent 13%),
      radial-gradient(ellipse at 10% 55%, var(--sage) 0 20%, transparent 21%),
      radial-gradient(ellipse at 85% 90%, var(--cocoa) 0 14%, transparent 15%),
      linear-gradient(200deg, var(--blush) 0%, var(--sage) 35%, var(--blush) 60%, var(--pink) 85%, var(--sage) 100%);
  }
  .pouch__zip {
    position: absolute; left: 0; right: 0; top: 36px; height: 6px;
    border-top: 1px solid rgba(255,255,255,0.55);
    border-bottom: 1px solid rgba(255,255,255,0.35);
  }

  .label {
    position: absolute;
    left: 41px; top: 103px;
    width: 275px; height: 370px;
    background: var(--label);
    text-align: center;
  }

  /* front label */
  .brand {
    font-family: "Quicksand", sans-serif;
    font-weight: 500;
    font-size: 30px;
    line-height: 1.1;
    margin-top: 42px;
  }
  .product-type { font-size: 12px; margin-top: 8px; }
  .rule { height: 1px; background: var(--plum-soft); margin: 0 15px; }
  .rule--top { margin-top: 15px; }
  .flavour {
    font-family: "Sofia Sans Extra Condensed", sans-serif;
    font-weight: 300;
    font-size: 40px;
    line-height: 1;
    padding: 8px 0 8px;
  }
  .claims {
    display: flex; justify-content: space-between;
    margin: 24px 26px 0;
    list-style: none;
  }
  .claim { width: 52px; font-size: 7px; line-height: 1.2; }
  .claim__icon {
    display: block; width: 30px; height: 30px; margin: 0 auto 6px;
  }
  .clay-rule { margin-top: 18px; }
  .clay { font-size: 12px; letter-spacing: 0.3px; padding: 8px 0 7px; }
  .net {
    position: absolute; left: 0; right: 0; bottom: 18px;
    font-size: 7.5px; line-height: 1.7;
  }

  /* back label */
  .back-title { font-size: 15px; font-weight: 600; margin-top: 44px; }
  .back-intro { font-size: 6.5px; line-height: 1.4; margin: 4px 22px 0; }
  .section-title { font-size: 17px; font-weight: 600; margin-top: 26px; }
  .steps { display: flex; justify-content: space-between; margin: 12px 14px 0; list-style: none; }
  .step { width: 76px; font-size: 5.5px; line-height: 1.35; }
  .step__number {
    display: block; width: 13px; height: 13px; border-radius: 50%;
    background: var(--plum); color: #fff;
    font-size: 7px; line-height: 13px; margin: 0 auto 6px;
  }
  .step:nth-child(2) { margin-top: 14px; }
  .step:nth-child(3) { margin-top: 28px; }
  .ingredients-title { margin-top: 20px; }
  .ingredients { font-size: 7.5px; line-height: 1.45; margin: 8px 20px 0; text-align: justify; }
</style>
</head>
<body>

<section class="pouch pouch--front" aria-label="Front of pouch">
  <div class="pouch__artwork" role="img" aria-label="Pastel illustration of palm leaves, coffee beans and chocolate pieces in pink, sage and tan"></div>
  <div class="pouch__zip"></div>
  <div class="label">
    <h1 class="brand">Brin’s Beauty</h1>
    <p class="product-type">Recycled Coffee scrub</p>
    <div class="rule rule--top"></div>
    <h2 class="flavour">Coconut and Chocolate</h2>
    <div class="rule"></div>
    <ul class="claims">
      <li class="claim">
        <svg class="claim__icon" viewBox="0 0 30 30" aria-hidden="true">
          <circle cx="15" cy="15" r="15" fill="var(--plum)"/>
          <path d="M9 17a6 6 0 0 1 10-7M21 13a6 6 0 0 1-10 7" fill="none" stroke="#fff" stroke-width="1.2"/>
          <path d="M19 7v3h-3M11 23v-3h3" fill="none" stroke="#fff" stroke-width="1.2"/>
        </svg>
        Recycled packaging
      </li>
      <li class="claim">
        <svg class="claim__icon" viewBox="0 0 30 30" aria-hidden="true">
          <circle cx="15" cy="15" r="15" fill="var(--plum)"/>
          <path d="M15 7c5 3 5 12 0 16c-5-4-5-13 0-16z M15 10v13" fill="none" stroke="#fff" stroke-width="1.2"/>
        </svg>
        Vegan
      </li>
      <li class="claim">
        <svg class="claim__icon" viewBox="0 0 30 30" aria-hidden="true">
          <circle cx="15" cy="15" r="15" fill="var(--plum)"/>
        </svg>
        Not tested on animal
      </li>
      <li class="claim">
        <svg class="claim__icon" viewBox="0 0 30 30" aria-hidden="true">
          <circle cx="15" cy="15" r="15" fill="var(--plum)"/>
          <ellipse cx="15" cy="15" rx="5" ry="7.5" fill="none" stroke="#fff" stroke-width="1.2"/>
          <path d="M15 8c-2 4 2 10 0 14" fill="none" stroke="#fff" stroke-width="1.2"/>
        </svg>
        Recycled coffee
      </li>
    </ul>
    <div class="rule clay-rule"></div>
    <p class="clay">PINK AUSTRALIAN CLAY</p>
    <div class="rule"></div>
    <p class="net">150g 5.29 oz<br>Made in Australia</p>
  </div>
</section>

<section class="pouch pouch--back" aria-label="Back of pouch">
  <div class="pouch__artwork" role="img" aria-label="Pastel illustration of palm leaves, coffee beans and chocolate pieces in pink, sage and tan"></div>
  <div class="pouch__zip"></div>
  <div class="label">
    <h2 class="back-title">Recycled Coffee scrub</h2>
    <p class="back-intro">Lorem ipsum dolor sit amet, consectetuer adipiscing elit, sed diam nonummy nibh euismod tincidunt ut laoreet dolore magna aliquam erat</p>
    <h3 class="section-title">How to use:</h3>
    <ol class="steps">
      <li class="step"><span class="step__number">1</span>Lorem ipsum dolor sit amet, consectetuer adipiscing elit, sed diam nonummy nibh euismod tincidunt ut laoreet</li>
      <li class="step"><span class="step__number">2</span>Lorem ipsum dolor sit amet, consectetuer adipiscing elit, sed diam nonummy nibh euismod tincidunt ut laoreet</li>
      <li class="step"><span class="step__number">3</span>Lorem ipsum dolor sit amet, consectetuer adipiscing elit, sed diam nonummy nibh euismod tincidunt ut laoreet</li>
    </ol>
    <h3 class="section-title ingredients-title">Ingredients:</h3>
    <p class="ingredients">Lorem ipsum dolor sit amet, consectetuer adipiscing elit, sed diam nonummy nibh euismod tincidunt ut laoreet dolore magna aliquam erat volutpat. Ut wisi enim ad minim veniam, quis nostrud exerci tation ullamcorper suscipit lobortis nisl ut aliquip ex ea commodo</p>
  </div>
</section>

</body>
</html>
```